zQuandaro Marketing - SEM, Influencer website. FUN RETRO VIBES.

I included content. Need an advertising website that displays, my services, blog and about me and contact.
I need to be able to easily update content, blogs by myself. Need it to be a Wordpress. I included some content pages. Please let me know if this give a better idea of what I do and the tone I am looking for.
Target Market(s)
Small Business Entrepreneurs, Start-ups, Male and Female ages 25-50
Industry/Entity Type
Advertising
Coding
Coded - Design and coding required
Number of Pages Required
3 page
Font styles to use
Other font styles liked:
- Lazer 64
Requirements
Must have
- Services, Blog, About Me, Contact. Creative Design is really what I want. Unique and fun imagery. I like the 80's style of design. Retro colors, in the logo. LAzer 84 font is cool. Hex colors should be in the brief. MUST LOOK GOOD ON MOBILE. The mobile experience has to be good.
Nice to have
- I am open minded to new creative ideas.
Hex Code
#000205
#3978A3
#5BF8FB
#7B7BFB
#5CC9EC
#AB63FA
Should not have
- Cookie Cutter feel. They made me choose the color wheel but the colors I want are on the brief. Please let me know if you need more logo images, images of me

```html
<!DOCTYPE html>
<html lang="en">
<head>
<meta charset="utf-8">
<title>zQuandaro Marketing</title>
<link rel="stylesheet" href="https://fonts.googleapis.com/css2?family=Montserrat:wght@700;800&family=Rajdhani:wght@500;700&display=swap">
<style>
  :root {
    --ink: #000205;
    --white: #ffffff;
    --steel-blue: #3978a3;
    --deep-blue: #1c2f52;
    --mist: #c9ced6;
    --neon-cyan: #5cc9ec;
    --violet: #ab63fa;
    --footer-text: #7a7a7a;
    --footer-bg: #ffffff;
  }
  * { margin: 0; padding: 0; box-sizing: border-box; }
  html, body {
    width: 1200px;
    height: 942px;
    overflow: hidden;
    background: var(--footer-bg);
  }
  .page {
    position: relative;
    width: 1200px;
    height: 942px;
  }
  .hero {
    position: relative;
    width: 1200px;
    height: 898px;
    overflow: hidden;
  }
  .hero-photo {
    position: absolute;
    inset: 0;
    background:
      linear-gradient(180deg, rgba(0,2,5,0.92) 0%, rgba(0,2,5,0.55) 14%, rgba(0,2,5,0) 34%),
      radial-gradient(ellipse 260px 200px at 960px 470px, rgba(240,160,90,0.55), rgba(240,160,90,0) 70%),
      radial-gradient(ellipse 420px 260px at 820px 300px, rgba(225,228,234,0.85), rgba(225,228,234,0) 72%),
      radial-gradient(ellipse 360px 520px at 180px 520px, rgba(57,120,163,0.85), rgba(57,120,163,0) 75%),
      linear-gradient(100deg, #1d3a66 0%, #35507a 35%, #6d7b92 60%, #9aa3b2 80%, #596a86 100%);
  }
  .site-header {
    position: absolute;
    top: 0; left: 0; right: 0;
    height: 160px;
  }
  .brand {
    position: absolute;
    left: 24px;
    top: 28px;
    display: flex;
    flex-direction: column;
    align-items: center;
    gap: 6px;
  }
  .brand-mark {
    width: 80px;
    height: 80px;
    border: 2px solid var(--neon-cyan);
    border-radius: 50%;
  }
  .brand-name {
    font-family: "Rajdhani", sans-serif;
    font-weight: 500;
    font-size: 22px;
    letter-spacing: 1px;
    color: var(--neon-cyan);
  }
  .main-nav {
    position: absolute;
    right: 25px;
    top: 72px;
    display: flex;
    gap: 17px;
    list-style: none;
  }
  .main-nav a {
    font-family: "Rajdhani", sans-serif;
    font-weight: 700;
    font-size: 15px;
    color: var(--white);
    text-decoration: none;
    letter-spacing: 0.2px;
  }
  .main-nav li:first-child { margin-right: 6px; }
  .intro-panel {
    position: absolute;
    left: 206px;
    top: 406px;
    width: 787px;
    height: 243px;
    border: 1px solid rgba(255,255,255,0.85);
    border-radius: 4px;
    background: linear-gradient(90deg, rgba(0,2,5,1) 0%, rgba(0,2,5,0.82) 30%, rgba(0,2,5,0.45) 70%, rgba(0,2,5,0.2) 100%);
    padding: 58px 40px 0 47px;
    color: var(--white);
  }
  .intro-title {
    font-family: "Montserrat", sans-serif;
    font-weight: 800;
    font-size: 34px;
    line-height: 38px;
    letter-spacing: 0.3px;
  }
  .intro-text {
    font-family: "Montserrat", sans-serif;
    font-weight: 700;
    font-size: 22.5px;
    line-height: 31.5px;
    margin-top: 2px;
  }
  .site-footer {
    height: 44px;
    display: flex;
    align-items: center;
    justify-content: center;
    background: var(--footer-bg);
    font-family: "Rajdhani", sans-serif;
    font-weight: 500;
    font-size: 15px;
    color: var(--footer-text);
  }
</style>
</head>
<body>
<div class="page">
  <section class="hero">
    <div class="hero-photo" role="img" aria-label="Blurred photo of a businessman touching glowing jigsaw puzzle pieces, with faint business icons in the background"></div>
    <header class="site-header">
      <div class="brand">
        <span class="brand-mark"></span>
        <span class="brand-name">zQuandaro</span>
      </div>
      <ul class="main-nav">
        <li><a href="#">HOME</a></li>
        <li><a href="#">ABOUT</a></li>
        <li><a href="#">SERVICES</a></li>
        <li><a href="#">BLOG</a></li>
        <li><a href="#">NEWS</a></li>
        <li><a href="#">CONTACT</a></li>
      </ul>
    </header>
    <div class="intro-panel">
      <h1 class="intro-title">LET zQUANDARO GUIDE YOU!</h1>
      <p class="intro-text">Lorem ipsum dolor sit amet, consectetur adipiscing elit, sed do eiusmod tempor incididunt ut labore et dolore magna aliqua. Ut enim ad minim veniam.</p>
    </div>
  </section>
  <footer class="site-footer">© 2020 zQuandaro. All Rights Reserved.</footer>
</div>
</body>
</html>
```